Letterhead Design Project

Standard A4 paper, center the name Sparkwell Tidy (with the mop) same as front of business card.
748 Harbourview Rd Lindenvale 5087 ABN: 71326094518
M. 0428163904 T. 83917564 Calibri font

Industry/Entity Type

Business

```html
<!DOCTYPE html>
<html lang="en">
<head>
<meta charset="utf-8">
<title>Sparkwell Tidy – Letterhead</title>
<link rel="stylesheet" href="https://fonts.googleapis.com/css2?family=Carlito:wght@400;700&family=Didact+Gothic&display=swap">
<style>
  :root {
    --backdrop: #dcdcdc;
    --paper: #ececec;
    --brand-blue: #2d6399;
    --ink: #8a8a8a;
    --ink-dark: #555555;
    --ink-soft: #a3a3a3;
    --panel: #e0e0e0;
    --table-head: #bccbd6;
    --table-head-ink: #eef3f7;
    --row-alt: #e3e3e3;
    --tab-grey: #b5b5b5;
    --rule: #9a9a9a;
  }
  * { box-sizing: border-box; margin: 0; padding: 0; }
  html, body {
    width: 1200px; height: 746px; overflow: hidden;
    background: var(--backdrop);
  }
  .canvas { position: relative; width: 1200px; height: 746px; overflow: hidden; }

  .letterhead {
    position: absolute; left: 150px; top: 30px;
    width: 900px; height: 1273px;
    background: var(--paper);
    box-shadow: 0 4px 18px rgba(0,0,0,0.08);
    font-family: "Didact Gothic", "Century Gothic", sans-serif;
    color: var(--ink);
  }
  .edge-tab { position: absolute; }
  .edge-tab--brand { left: 0; top: 70px; width: 30px; height: 38px; background: var(--brand-blue); }
  .edge-tab--side { right: 0; top: 430px; width: 18px; height: 44px; background: var(--tab-grey); }

  .brand {
    position: absolute; left: 0; right: 0; top: 62px;
    display: flex; justify-content: center; align-items: center; gap: 16px;
  }
  .brand-mark {
    width: 34px; height: 34px; border-radius: 50%;
    background: var(--brand-blue);
  }
  .business-name {
    font-family: "Carlito", "Calibri", sans-serif;
    font-weight: 400; font-size: 50px; line-height: 1; letter-spacing: -0.5px;
    color: var(--brand-blue); text-transform: uppercase;
  }

  .contact-bar {
    position: absolute; right: 60px; top: 150px;
    display: flex; align-items: center; gap: 26px;
    font-size: 15px; line-height: 1.4;
  }
  .contact-bar address { font-style: normal; color: var(--ink); }
  .contact-bar .divider { width: 1px; height: 58px; background: var(--rule); }
  .contact-bar .phones { color: var(--ink-dark); }
  .contact-bar .label {
    font-family: "Carlito", "Calibri", sans-serif; font-weight: 700;
    color: var(--brand-blue);
  }

  .invoice-panel {
    position: absolute; left: 70px; top: 230px;
    width: 240px; height: 400px;
    background: var(--panel);
    padding: 30px 26px;
    font-size: 14px; line-height: 1.55; color: var(--ink-soft);
  }
  .invoice-panel h2 { font-weight: 400; font-size: 20px; margin-bottom: 18px; color: var(--ink); }
  .invoice-panel p { margin-bottom: 16px; }

  .letter-body { position: absolute; left: 340px; top: 272px; width: 500px; }
  .letter-body h1 { font-weight: 400; font-size: 21px; color: var(--ink); margin-bottom: 12px; }
  .letter-body .intro { font-size: 13.5px; line-height: 1.5; color: var(--ink-soft); margin-bottom: 22px; }

  .services { width: 100%; border-collapse: collapse; font-size: 13.5px; color: var(--ink); }
  .services th {
    background: var(--table-head); color: var(--table-head-ink);
    font-weight: 400; text-align: left; padding: 12px 14px; height: 74px; vertical-align: bottom;
  }
  .services td { padding: 9px 14px; }
  .services tbody tr:nth-child(odd) td { background: var(--row-alt); }
  .services .col-cost { width: 70px; }
  .services .col-date { width: 80px; }
</style>
</head>
<body>
<main class="canvas">
  <article class="letterhead">
    <span class="edge-tab edge-tab--brand"></span>
    <span class="edge-tab edge-tab--side"></span>

    <header class="brand">
      <span class="brand-mark" role="img" aria-label="Sparkwell Tidy mop mark"></span>
      <div class="business-name">Sparkwell Tidy</div>
    </header>

    <div class="contact-bar">
      <address>748 Harbourview Rd<br>Lindenvale 5087<br>ABN: 71326094518</address>
      <span class="divider"></span>
      <div class="phones">
        <span class="label">Mobile:</span> 0428163904<br>
        <span class="label">Phone:</span> 83917564
      </div>
    </div>

    <aside class="invoice-panel">
      <h2>Invoice</h2>
      <p>418 Corbel Ave.<br>Suite 212<br>Fairmount, FL 30412</p>
      <p>Phone / 1.555.0148<br>Email /<br>sparkwellmail.com<br>Fax / 1.555.0172<br>Web /<br>sparkwelltidy.com<br>Date / July 4, 2009<br>To / Mr Alan Pryce<br>From / Your Name</p>
    </aside>

    <section class="letter-body">
      <h1>Thank You for Your Business!</h1>
      <p class="intro">Gismodi atonsent nibh el deliquat at. Duis nos non veriusci tincip ero odionum quip esto odoluptat. Duip et nos adip ex euisi ex euisis nonum numsan vullumsan euisse diam, volorpercil euipsuscinim doloreetum zzriusci te feu facin velestrud magna consequis nonulput lan veros augiamet atu. As re con porem et, quam as molorempor rest, omnimus, excest aut laut quam ipsus deriti sitium sit facerit, quam qui.</p>
      <table class="services">
        <thead>
          <tr><th>Service Rendered</th><th class="col-cost">Cost</th><th class="col-date">Date</th></tr>
        </thead>
        <tbody>
          <tr><td>Gismodi atonsent nibh el deliquat at. Duis nos non</td><td>$000</td><td>01/01/11</td></tr>
          <tr><td>Gismodi atonsent nibh el deliquat at. Duis nos non</td><td>$000</td><td>01/01/11</td></tr>
          <tr><td>Gismodi atonsent nibh el deliquat at. Duis nos non</td><td>$000</td><td>01/01/11</td></tr>
          <tr><td>Gismodi atonsent nibh el deliquat at. Duis nos non</td><td>$000</td><td>01/01/11</td></tr>
          <tr><td>Gismodi atonsent nibh el deliquat at. Duis nos non</td><td>$000</td><td>01/01/11</td></tr>
          <tr><td>Gismodi atonsent nibh el deliquat at. Duis nos non</td><td>$000</td><td>01/01/11</td></tr>
        </tbody>
      </table>
    </section>
  </article>
</main>
</body>
</html>
```